One page sales fact sheet for data consultancy company

We need a serious and professional looking 1-page fact sheet that we want to send over to potential clients via email.
The upper part should consists of a header, the client logo and 3 charts.
(1 chart with 5 datapoints / 1 chart with 3 bubbles and percentage in it, 1 chart with numbers and text)
In the lower part there should be some text description about our company and a big chart consisting of a table (see drawing).
See attached drawing to get a better understanding of the whole idea.
The fact sheet should be catchy but professional in the same way.
Colors your choice but classic, i.e. black/white/grey/blue
The contest winner can expect more work from us based on the winning design.
*Please note that the logo reflects our original logo style but is not our
actual company name for privacy reasons

```html
<!DOCTYPE html>
<html lang="en">
<head>
<meta charset="utf-8">
<title>Norvik – Market Analysis Fact Sheet</title>
<link rel="stylesheet" href="https://fonts.googleapis.com/css2?family=Archivo:ital,wght@0,300;1,300;1,800&family=Montserrat:wght@300;400;700&family=Source+Sans+3:wght@400&display=swap">
<style>
  :root {
    --ink: #222833;
    --grid: #3a4150;
    --paper: #ffffff;
    --cyan: #96e0e2;
    --grey: #96979b;
    --label: #e6e7e9;
  }
  * { margin: 0; padding: 0; box-sizing: border-box; }
  html, body { width: 850px; height: 1200px; overflow: hidden; background: var(--paper); }
  .sheet { position: relative; width: 850px; height: 1200px; background: var(--paper); color: var(--paper); font-family: "Montserrat", sans-serif; }

  .header-art { position: absolute; left: 0; top: 0; }
  .brand-name {
    position: absolute; left: 0; width: 850px; top: 74px; line-height: 62px; text-align: center;
    font-family: "Montserrat", sans-serif; font-weight: 700; font-size: 62px; color: var(--paper);
  }

  .body-panel { position: absolute; left: 0; top: 197px; width: 850px; height: 920px; background: var(--ink); }

  .spaced-title {
    position: absolute; font-family: "Montserrat", sans-serif; font-weight: 300; text-align: center;
    color: var(--paper); white-space: nowrap; line-height: 1;
  }
  .section-title { left: 0; width: 850px; top: 257px; font-size: 27px; letter-spacing: 8px; padding-left: 8px; }
  .chart-title { left: 167px; top: 346px; font-size: 22px; letter-spacing: 9px; }
  .types-title { left: 481px; top: 346px; font-size: 24px; letter-spacing: 6px; }
  .competitors-title { left: 0; width: 850px; top: 884px; font-size: 25px; letter-spacing: 7px; padding-left: 7px; }

  .bar-chart { position: absolute; left: 106px; top: 317px; }
  .divider-v { position: absolute; left: 422px; top: 329px; width: 2px; height: 131px; background: var(--paper); }

  .share-box { position: absolute; top: 406px; width: 116px; height: 54px; }
  .share-box svg { position: absolute; left: 0; top: 0; }
  .share-value {
    position: absolute; left: 0; top: 0; width: 116px; line-height: 54px; text-align: center;
    font-family: "Archivo", sans-serif; font-style: italic; font-weight: 800; font-size: 41px; color: var(--paper);
  }
  .share-value sup { font-size: 21px; vertical-align: 15px; }

  .stat-number {
    position: absolute; top: 528px; text-align: center; width: 240px; line-height: 56px;
    font-family: "Archivo", sans-serif; font-style: italic; font-weight: 300; font-size: 53px; color: var(--paper);
  }
  .stat-plates { position: absolute; left: 0; top: 593px; }
  .stat-label {
    position: absolute; top: 593px; height: 26px; line-height: 27px; text-align: center; white-space: nowrap;
    font-family: "Archivo", sans-serif; font-style: italic; font-weight: 800; font-size: 20px; color: var(--ink);
  }

  .sales-frame { position: absolute; left: 0; top: 0; }
  .sales-total {
    position: absolute; left: 137px; width: 560px; top: 648px; text-align: center; line-height: 46px;
    font-family: "Archivo", sans-serif; font-style: italic; font-weight: 800; font-size: 40px; color: var(--paper);
  }

  .company-blurb {
    position: absolute; left: 126px; width: 600px; top: 757px; text-align: center;
    font-family: "Source Sans 3", sans-serif; font-size: 13.3px; line-height: 16.2px; color: var(--paper);
  }

  .layer-label {
    position: absolute; top: 938px; width: 120px; text-align: center;
    font-family: "Montserrat", sans-serif; font-size: 12px; letter-spacing: 2px; color: var(--paper);
  }
  .layer-divider { position: absolute; top: 922px; width: 2px; height: 40px; background: var(--paper); }

  .level-item {
    position: absolute; top: 1010px; display: flex; align-items: center; gap: 7px;
    font-family: "Montserrat", sans-serif; font-size: 13px; letter-spacing: 1.4px; color: var(--paper);
  }
</style>
</head>
<body>
<main class="sheet">

  <svg class="header-art" width="850" height="197" viewBox="0 0 850 197" aria-hidden="true">
    <polygon points="0,19 181,19 72,186 0,186" fill="var(--ink)"/>
    <polygon points="199,17 850,19 850,186 85,186" fill="var(--ink)"/>
  </svg>
  <div class="brand-name">NORVIK</div>

  <section class="body-panel"></section>

  <h1 class="spaced-title section-title">MARKET ANALYSIS</h1>

  <svg class="bar-chart" width="277" height="152" viewBox="0 0 277 152" role="img" aria-label="Bar chart of five yearly data points">
    <g stroke="var(--grid)" stroke-width="1">
      <line x1="0" y1="38" x2="277" y2="38"/>
      <line x1="0" y1="76" x2="277" y2="76"/>
      <line x1="0" y1="114" x2="277" y2="114"/>
    </g>
    <rect x="18"  y="118" width="32" height="34"  fill="var(--grey)"/>
    <rect x="70"  y="96"  width="32" height="56"  fill="var(--cyan)"/>
    <rect x="122" y="72"  width="32" height="80"  fill="var(--paper)"/>
    <rect x="174" y="48"  width="32" height="104" fill="var(--cyan)"/>
    <rect x="226" y="24"  width="32" height="128" fill="var(--paper)"/>
    <line x1="0" y1="151" x2="277" y2="151" stroke="var(--paper)" stroke-width="1.5"/>
  </svg>
  <h2 class="spaced-title chart-title">DATA</h2>

  <div class="divider-v"></div>

  <h2 class="spaced-title types-title">PRODUCT TYPES</h2>

  <div class="share-box" style="left:449px;">
    <svg width="116" height="54" viewBox="0 0 116 54" aria-hidden="true"><polygon points="20,1 115,1 96,53 1,53" fill="none" stroke="var(--cyan)" stroke-width="1.6"/></svg>
    <div class="share-value">40<sup>%</sup></div>
  </div>
  <div class="share-box" style="left:564px;">
    <svg width="116" height="54" viewBox="0 0 116 54" aria-hidden="true"><polygon points="20,1 115,1 96,53 1,53" fill="none" stroke="var(--cyan)" stroke-width="1.6"/></svg>
    <div class="share-value">30<sup>%</sup></div>
  </div>
  <div class="share-box" style="left:680px;">
    <svg width="116" height="54" viewBox="0 0 116 54" aria-hidden="true"><polygon points="20,1 115,1 96,53 1,53" fill="none" stroke="var(--cyan)" stroke-width="1.6"/></svg>
    <div class="share-value">20<sup>%</sup></div>
  </div>

  <div class="stat-number" style="left:139px;">20</div>
  <div class="stat-number" style="left:281px;">150</div>
  <div class="stat-number" style="left:474px;">350,000</div>

  <svg class="stat-plates" width="850" height="30" viewBox="0 593 850 30" aria-hidden="true">
    <polygon points="180,593 320,593 308,619 169,619" fill="var(--label)"/>
    <polygon points="334,593 474,593 462,619 323,619" fill="var(--label)"/>
    <polygon points="494,593 712,593 700,619 482,619" fill="var(--label)"/>
  </svg>
  <div class="stat-label" style="left:169px;width:145px;">VENDORS</div>
  <div class="stat-label" style="left:323px;width:145px;">PRODUCTS</div>
  <div class="stat-label" style="left:488px;width:218px;">AVAILABLE ITEMS</div>

  <svg class="sales-frame" width="850" height="720" viewBox="0 0 850 720" aria-hidden="true">
    <polygon points="170,630 697,630 665,712 137,712" fill="none" stroke="var(--paper)" stroke-width="1.6"/>
  </svg>
  <div class="sales-total">40 MILLION IN SALES</div>

  <p class="company-blurb">Lorem ipsum dolor sit amet, consectetuer adipiscing elit, sed diam nonummy nibh euismod tincidunt ut<br>laoreet dolore magna aliquam erat volutpat. Ut wisi enim ad minim veniam, quis nostrud exerci tation<br>ullamcorper suscipit lobortis nisl ut aliquip ex ea commodo consequat. Duis autem vel eum iriure dolor<br>in hendrerit in vulputate velit esse molestie consequat, vel illum</p>

  <h2 class="spaced-title competitors-title">COMPETITORS</h2>

  <div class="layer-label" style="left:127px;">LAYER 1</div>
  <div class="layer-divider" style="left:265px;"></div>
  <div class="layer-label" style="left:285px;">LAYER 2</div>
  <div class="layer-divider" style="left:427px;"></div>
  <div class="layer-label" style="left:443px;">LAYER 3</div>
  <div class="layer-divider" style="left:589px;"></div>
  <div class="layer-label" style="left:601px;">LAYER 4</div>

  <div class="level-item" style="left:216px;">
    <svg width="28" height="26" viewBox="0 0 28 26" aria-hidden="true" fill="none" stroke="var(--paper)" stroke-width="1.4">
      <circle cx="14" cy="7" r="6"/>
      <path d="M1,25 C3,17 9,14 14,14 C19,14 25,17 27,25"/>
    </svg>
    <span>User Level</span>
  </div>
  <div class="level-item" style="left:350px;">
    <svg width="24" height="24" viewBox="0 0 24 24" aria-hidden="true" fill="none" stroke="var(--paper)" stroke-width="1.3">
      <path d="M4,4 C14,3 22,11 22,22"/>
      <circle cx="3" cy="21" r="1.8"/>
      <path d="M5,19 L14,11" stroke-dasharray="2 3"/>
    </svg>
    <span>Entity Level</span>
  </div>
  <div class="level-item" style="left:497px;">
    <svg width="26" height="24" viewBox="0 0 26 24" aria-hidden="true" fill="none" stroke="var(--paper)" stroke-width="1.3">
      <path d="M14,20 H2 V2 H20 V11"/>
      <path d="M6,7 H15 M6,12 H13 M6,16 H11 M9,5 V18"/>
      <circle cx="19" cy="17" r="5.5"/>
      <path d="M19,14 V20 M16,17 H22"/>
    </svg>
    <span>Personal Level</span>
  </div>

</main>
</body>
</html>
```